Business Cards and label design needed!

I am a metalsmith, working in sterling silver, brass and moving slowly into adding some gold accent pieces. I also use patinas to add color to brass pieces. The peacock feather is used in my packaging, as both a label and tissue paper. I am attaching what I am currently using, and printing at home, but I need a design that I can have professionally printed. My website is www.willowharborcrafts.com
Target Market(s)
Established Professionals, Independent thinkers, Art donors, Artist supporters
Industry/Entity Type
Jewelry
Contact Information for Business Card
I would like a business card with the basic contact information, including Facebook and Instagram. I currently use a peacock feather and would like to continue that. I like to use turquoise, Tiffany blue and colors in that direction. I am open to other suggestions. I would like to be able to transfer the design to oval labels as well.
Font styles to use
Other font styles liked:
- Garamond or other fonts that have a slight script that is easy to read
Look and feel

```html
<!DOCTYPE html>
<html lang="en">
<head>
<meta charset="utf-8">
<title>Willow Harbor Crafts — Business Card</title>
<link href="https://fonts.googleapis.com/css2?family=Italianno&family=Roboto:wght@400;700&family=Roboto+Condensed:wght@700&display=swap" rel="stylesheet">
<style>
  :root {
    --stage: #2b2b2d;
    --indigo: #1f26a8;
    --indigo-deep: #161c86;
    --indigo-light: #3340c4;
    --teal: #14959a;
    --teal-deep: #0f8589;
    --ink-light: #ffffff;
    --icon-teal: #2bbfb3;
  }
  * { box-sizing: border-box; margin: 0; padding: 0; }
  html, body { width: 1200px; height: 911px; overflow: hidden; background: var(--stage); }
  .canvas {
    position: relative; width: 1200px; height: 911px;
    display: flex; align-items: center; justify-content: center; gap: 60px;
  }
  .card {
    position: relative; width: 525px; height: 300px; border-radius: 4px;
    box-shadow: 0 14px 30px rgba(0,0,0,.45);
    color: var(--ink-light); overflow: hidden;
  }
  .card--front { background: linear-gradient(135deg, var(--indigo-light) 0%, var(--indigo) 45%, var(--indigo-deep) 100%); }
  .card--back { background: linear-gradient(160deg, var(--teal) 0%, var(--teal-deep) 100%); }

  .brand { position: absolute; left: 38px; top: 62px; display: flex; align-items: center; gap: 12px; }
  .brand__dot { width: 16px; height: 16px; border-radius: 50%; background: var(--icon-teal); }
  .brand__name { font-family: "Italianno", cursive; font-size: 46px; line-height: 1; font-weight: 400; }

  .holder {
    position: absolute; right: 40px; top: 44px;
    font-family: "Roboto Condensed", sans-serif; font-weight: 700;
    font-size: 22px; letter-spacing: .5px; text-transform: uppercase;
  }

  .contact { position: absolute; left: 40px; bottom: 34px; list-style: none;
    font-family: "Roboto", sans-serif; font-size: 15px; line-height: 24px; }
  .contact__item { display: flex; align-items: center; gap: 8px; }
  .contact__item svg { width: 13px; height: 13px; flex: none; }
  .contact__item--plain { padding-left: 21px; }

  .back__name { position: absolute; left: 42px; bottom: 92px;
    font-family: "Italianno", cursive; font-size: 62px; line-height: 1; }
  .back__web { position: absolute; left: 46px; bottom: 52px;
    font-family: "Roboto", sans-serif; font-weight: 700; font-size: 18px; letter-spacing: .5px; }
</style>
</head>
<body>
<main class="canvas">
  <section class="card card--front" aria-label="Business card front">
    <div class="brand">
      <span class="brand__dot"></span>
      <span class="brand__name">Willow Harbor Crafts</span>
    </div>
    <div class="holder">Maren Holt</div>
    <ul class="contact">
      <li class="contact__item contact__item--plain">Alder Springs, TX 75501</li>
      <li class="contact__item">
        <svg viewBox="0 0 16 16" aria-hidden="true"><path fill="var(--icon-teal)" d="M3 1l3 3-2 2c1 2 3 4 5 5l2-2 3 3-2 3C7 15 1 9 1 3z"/></svg>
        555-014-2297
      </li>
      <li class="contact__item">
        <svg viewBox="0 0 16 16" aria-hidden="true"><rect x="1" y="3" width="14" height="10" rx="1" fill="var(--icon-teal)"/><path d="M1 4l7 5 7-5" stroke="var(--indigo)" stroke-width="1.5" fill="none"/></svg>
        studio@willowharborcrafts.com
      </li>
      <li class="contact__item">
        <svg viewBox="0 0 16 16" aria-hidden="true"><circle cx="8" cy="8" r="7" fill="var(--icon-teal)"/><path d="M1 8h14M8 1c-3 4-3 10 0 14M8 1c3 4 3 10 0 14" stroke="var(--indigo)" stroke-width="1" fill="none"/></svg>
        www.willowharborcrafts.com
      </li>
    </ul>
  </section>

  <section class="card card--back" aria-label="Business card back">
    <div class="back__name">Willow Harbor Crafts</div>
    <div class="back__web">www.willowharborcrafts.com</div>
  </section>
</main>
</body>
</html>
```